Quote Cards for Social Media RV

I would like to put these quotes over one of the pictures attached; One Quote per picture, and I want the quote to be bold or easy to read as well. I provided a few reference graphics that I really like as examples below. In very small letters at the bottom add @RVCarloweDaily

All of the pictures are attached; you can pick any photo and add one quote to it; but no stock photography

Target Market(s)

women trying to lose weight

Requirements
Must have
• quotes and pictures attached
Should not have
• no stock photography

```html
<!DOCTYPE html>
<html lang="en">
<head>
<meta charset="utf-8">
<title>Quote Cards for Social Media RV</title>
<link rel="stylesheet" href="https://fonts.googleapis.com/css2?family=Anton&family=Open+Sans:wght@400;500&family=Roboto+Condensed:wght@400&display=swap">
<style>
  :root {
    --page: #ffffff;
    --card: #0b0b0b;
    --quote-mark: #5c1b38;
    --headline: #ffffff;
    --accent: #f0509e;
    --small-text: #e6e6e6;
    --photo-light: #8a8a8a;
    --photo-dark: #1c1c1c;
  }
  * { margin: 0; padding: 0; box-sizing: border-box; }
  html, body {
    width: 806px; height: 1200px; overflow: hidden;
    background: var(--page);
  }
  .sheet { position: relative; width: 806px; height: 1200px; }
  .quote-card {
    position: absolute; width: 354px; height: 354px;
    background: var(--card); overflow: hidden;
  }
  .card-1 { left: 53px;  top: 53px; }
  .card-2 { left: 416px; top: 53px; }
  .card-3 { left: 53px;  top: 426px; }
  .card-4 { left: 416px; top: 426px; }
  .card-5 { left: 53px;  top: 799px; }

  .quote-mark {
    position: absolute; left: 9px; top: 0;
    width: 96px; height: 60px; z-index: 1;
  }
  .quote-mark path, .quote-mark circle { fill: var(--quote-mark); }
  .portrait {
    position: absolute; bottom: 0; z-index: 0;
    background: radial-gradient(ellipse at 50% 35%, var(--photo-light) 0%, #4a4a4a 45%, var(--photo-dark) 100%);
    border-radius: 45% 45% 0 0;
  }
  .headline {
    position: absolute; z-index: 2;
    font-family: "Anton", Impact, sans-serif;
    font-weight: 400;
    font-size: 30px; line-height: 32px; letter-spacing: -0.6px;
    color: var(--headline); text-transform: uppercase;
    white-space: nowrap;
  }
  .subline {
    position: absolute; z-index: 2;
    font-family: "Open Sans", Arial, sans-serif; font-weight: 400;
    font-size: 18px; line-height: 24px;
    color: var(--accent); text-transform: uppercase;
    white-space: nowrap;
  }
  .divider {
    position: absolute; z-index: 2; width: 25px; height: 1px;
    background: var(--accent);
  }
  .handle {
    position: absolute; z-index: 2;
    font-family: "Open Sans", Arial, sans-serif;
    font-size: 5px; color: var(--small-text);
  }
  .website {
    position: absolute; z-index: 2;
    font-family: "Roboto Condensed", Arial, sans-serif;
    font-size: 8px; color: var(--small-text);
  }
  .website-vertical {
    transform: rotate(-90deg); transform-origin: left top;
  }
</style>
</head>
<body>
<div class="sheet">

  <section class="quote-card card-1">
    <svg class="quote-mark" viewBox="0 0 96 60" aria-hidden="true">
      <circle cx="22" cy="38" r="20"/><path d="M3 34 C3 16 16 2 42 0 L43 7 C28 11 20 20 20 32 Z"/>
      <circle cx="72" cy="38" r="20"/><path d="M53 34 C53 16 66 2 92 0 L93 7 C78 11 70 20 70 32 Z"/>
    </svg>
    <div class="portrait" role="img" aria-label="Black and white photo of a woman in a cropped white sweater, dancing" style="left:134px; width:220px; top:150px;"></div>
    <h2 class="headline" style="left:28px; top:45px;">Wake up tomorrow<br>with a flatter<br>belly- yes</h2>
    <p class="subline" style="left:28px; top:149px;">This<br>overnight<br>remedy<br>works like<br>magic!</p>
    <span class="divider" style="left:28px; top:280px;"></span>
    <span class="handle" style="left:28px; top:283px;">@RVCarloweDaily</span>
    <span class="website" style="left:61px; top:325px;">www.yourwebsite.com</span>
  </section>

  <section class="quote-card card-2">
    <svg class="quote-mark" viewBox="0 0 96 60" aria-hidden="true">
      <circle cx="22" cy="38" r="20"/><path d="M3 34 C3 16 16 2 42 0 L43 7 C28 11 20 20 20 32 Z"/>
      <circle cx="72" cy="38" r="20"/><path d="M53 34 C53 16 66 2 92 0 L93 7 C78 11 70 20 70 32 Z"/>
    </svg>
    <div class="portrait" role="img" aria-label="Black and white photo of a woman in a fitted long-sleeve dress, in profile" style="left:190px; width:164px; top:0; border-radius:40% 40% 0 0;"></div>
    <h2 class="headline" style="left:22px; top:59px;">Finally-a natural<br>solution that<br>flattens your<br>belly and<br>eases stomach<br>bloat</h2>
    <span class="divider" style="left:22px; top:255px;"></span>
    <span class="handle" style="left:22px; top:258px;">@RVCarloweDaily</span>
    <span class="website website-vertical" style="left:330px; top:144px;">www.yourwebsite.com</span>
  </section>

  <section class="quote-card card-3">
    <svg class="quote-mark" viewBox="0 0 96 60" aria-hidden="true">
      <circle cx="22" cy="38" r="20"/><path d="M3 34 C3 16 16 2 42 0 L43 7 C28 11 20 20 20 32 Z"/>
      <circle cx="72" cy="38" r="20"/><path d="M53 34 C53 16 66 2 92 0 L93 7 C78 11 70 20 70 32 Z"/>
    </svg>
    <div class="portrait" role="img" aria-label="Black and white photo of a smiling woman in a turtleneck and high-waisted jeans" style="left:196px; width:158px; top:14px;"></div>
    <h2 class="headline" style="left:21px; top:77px;">One supplement,<br>one night</h2>
    <p class="subline" style="left:21px; top:155px;">Your belly bloat<br>could be gone<br>by morning.<br>Here's how it<br>works!</p>
    <span class="divider" style="left:21px; top:286px;"></span>
    <span class="handle" style="left:21px; top:290px;">@RVCarloweDaily</span>
    <span class="website" style="left:22px; top:320px;">www.yourwebsite.com</span>
  </section>

  <section class="quote-card card-4">
    <svg class="quote-mark" viewBox="0 0 96 60" aria-hidden="true">
      <circle cx="22" cy="38" r="20"/><path d="M3 34 C3 16 16 2 42 0 L43 7 C28 11 20 20 20 32 Z"/>
      <circle cx="72" cy="38" r="20"/><path d="M53 34 C53 16 66 2 92 0 L93 7 C78 11 70 20 70 32 Z"/>
    </svg>
    <div class="portrait" role="img" aria-label="Black and white photo of a smiling woman in a sheer mesh top, hand on hip" style="left:192px; width:162px; top:36px;"></div>
    <h2 class="headline" style="left:21px; top:50px;">Struggling with<br>bloating and<br>belly fat?</h2>
    <p class="subline" style="left:21px; top:150px;">Try this natural<br>solution<br>tonight, and<br>wake up feeling<br>lighter!</p>
    <span class="divider" style="left:21px; top:276px;"></span>
    <span class="handle" style="left:21px; top:280px;">@RVCarloweDaily</span>
    <span class="website" style="left:59px; top:319px;">www.yourwebsite.com</span>
  </section>

  <section class="quote-card card-5">
    <svg class="quote-mark" viewBox="0 0 96 60" aria-hidden="true">
      <circle cx="22" cy="38" r="20"/><path d="M3 34 C3 16 16 2 42 0 L43 7 C28 11 20 20 20 32 Z"/>
      <circle cx="72" cy="38" r="20"/><path d="M53 34 C53 16 66 2 92 0 L93 7 C78 11 70 20 70 32 Z"/>
    </svg>
    <div class="portrait" role="img" aria-label="Black and white photo of a woman in a dark top and light skirt, looking over her shoulder" style="left:170px; width:152px; top:46px;"></div>
    <h2 class="headline" style="left:22px; top:79px;">Sis, your<br>hormones are<br>out of whack</h2>
    <p class="subline" style="left:22px; top:178px;">That's why the<br>weight won't<br>budge!</p>
    <span class="divider" style="left:22px; top:258px;"></span>
    <span class="handle" style="left:22px; top:262px;">@RVCarloweDaily</span>
    <span class="website" style="left:22px; top:318px;">www.yourwebsite.com</span>
  </section>

</div>
</body>
</html>
```